Real Estate "For Sale" Sign for construction company

We need a sign that we can use to hang on a post and place on the road when we sell a property. The sign will be simple and will need to mainly feature our logo (files attached), as well as the words "For Sale", and then our phone number "(555) 617 3489". The sign will hang on a post that'll look something like the attached picture.

Target Market(s)

Home buyers

Industry/Entity Type

Real Estate

Font styles to use
Serif
Sans Serif

Colors
0054AA
0677BA
7BADD7
CADEEF
E8F1F8
0094D4
00A9DD
6FCCEA
C7EBF8
E9F6FB

Requirements
Must have
• For Sale & our phone number

```html
<!DOCTYPE html>
<html lang="en">
<head>
<meta charset="utf-8">
<title>For Sale Sign – Highland Ridge Properties</title>
<link rel="stylesheet" href="https://fonts.googleapis.com/css2?family=Archivo+Black&family=Montserrat:wght@400&display=swap">
<style>
  :root {
    --sale-red: #dc0606;
    --rule-blue: #0e79c0;
    --call-navy: #263a7a;
    --phone-navy: #141f49;
    --brand-blue: #1680c4;
    --brand-mark: #0677ba;
    --paper: #ffffff;
  }
  html, body {
    margin: 0;
    padding: 0;
    overflow: hidden;
    background: var(--paper);
  }
  .sign {
    display: block;
    width: 687px;
    height: 1200px;
  }
  .headline {
    font-family: "Archivo Black", "Arial Black", sans-serif;
    fill: var(--sale-red);
  }
  .call-line {
    font-family: "Archivo Black", "Arial Black", sans-serif;
    fill: var(--call-navy);
  }
  .phone {
    font-family: "Archivo Black", "Arial Black", sans-serif;
    fill: var(--phone-navy);
  }
  .brand-name, .brand-tagline {
    font-family: "Montserrat", Arial, sans-serif;
    font-weight: 400;
    fill: var(--brand-blue);
  }
  .headline-frame {
    fill: none;
    stroke: var(--sale-red);
    stroke-width: 8;
  }
  .divider {
    stroke: var(--rule-blue);
    stroke-width: 8;
  }
  .brand-dot {
    fill: var(--brand-mark);
  }
</style>
</head>
<body>
<svg class="sign" viewBox="0 0 1456 2560" preserveAspectRatio="none" xmlns="http://www.w3.org/2000/svg">
  <rect class="headline-frame" x="59" y="131" width="1342" height="852" rx="114" ry="114"/>
  <text class="headline" x="245" y="485" font-size="430" textLength="970" lengthAdjust="spacingAndGlyphs">FOR</text>
  <text class="headline" x="105" y="878" font-size="430" textLength="1250" lengthAdjust="spacingAndGlyphs">SALE</text>

  <line class="divider" x1="73" y1="1086" x2="1383" y2="1086"/>

  <text class="call-line" x="140" y="1271" font-size="116" textLength="1177" lengthAdjust="spacingAndGlyphs">CALL OR TEXT US AT:</text>

  <text class="phone" x="393" y="1612" font-size="290" textLength="710" lengthAdjust="spacingAndGlyphs">(555)</text>
  <text class="phone" x="92" y="1893" font-size="290" textLength="1312" lengthAdjust="spacingAndGlyphs">617 3489</text>

  <circle class="brand-dot" cx="720" cy="2095" r="100"/>
  <text class="brand-name" x="165" y="2297" font-size="128" textLength="1115" lengthAdjust="spacingAndGlyphs">Highland Ridge</text>
  <text class="brand-tagline" x="430" y="2368" font-size="40" textLength="580" lengthAdjust="spacing">PROPERTIES</text>
</svg>
</body>
</html>
```